CONTACT US Page and design for website

We need a contact us page for our website. We would like it to have a message area, a map, our information, etc.

Please see the text attachment for what we are looking for. We need to have something that is creative and interesting, modern and professional.

We believe that a contact US page should be very creative because everyone clicks that to contact us. We want it to be super professional, attention grabbing, pleasing to the eye.

PLEASE KEEP THE HEADER AND FOOTER THE SAME, ONLY THE ACTUAL CONTACT US PAGE NEEDS TO BE WORKED ON. THANKS!
We are excited to work with designers for this project.

Target Market(s)

Clients in technology business

Industry/Entity Type

Information Technology

Number of Pages Required

1 page

Font styles to use
Serif

Requirements
Must have
• CHECK THE TEXT ATTACHMENT PLEASE
• Must stay within our design colors and theme.
Nice to have
• see attachment
Should not have
• it should be special

```html
<!DOCTYPE html>
<html lang="en">
<head>
<meta charset="utf-8">
<title>Contact Us – Traxiven</title>
<link href="https://fonts.googleapis.com/css2?family=Roboto:wght@300;400;500;700&display=swap" rel="stylesheet">
<style>
:root{
  --teal:#2ec4b0;
  --teal-dark:#22a898;
  --teal-band:#35c9b6;
  --ink:#222;
  --line:#e3e3e3;
  --field:#f1f1f1;
  --foot:#a4a4a4;
  --foot-dark:#989898;
  --white:#fff;
}
*{box-sizing:border-box;margin:0;padding:0}
html,body{width:702px;height:1200px;overflow:hidden}
body{font-family:"Roboto",Arial,sans-serif;color:var(--ink);background:var(--white);position:relative}
.abs{position:absolute}

/* header */
.account-tab{left:537px;top:0;width:118px;height:20px;background:#9b9b9b;border-radius:0 0 14px 14px;display:flex;font-size:7px;color:#333}
.account-tab span{flex:1;display:flex;align-items:center;justify-content:center}
.account-tab span+span{background:#b5b5b5;border-radius:0 0 14px 0}
.brand{left:45px;top:20px;display:flex;align-items:center;gap:10px}
.brand-mark{width:30px;height:30px;background:var(--teal)}
.brand-name{font-size:22px;font-weight:500;letter-spacing:3px;color:var(--teal-dark);line-height:1}
.contact-quick{top:30px;display:flex;align-items:center;gap:8px;font-size:9px;color:#555}
.icon-ring{width:24px;height:24px;border-radius:50%;border:1px solid #cfd;background:#fff;display:flex;align-items:center;justify-content:center;box-shadow:0 0 0 2px #eef}
.phone-big{font-size:12px;color:#333}
.nav{top:61px;left:0;width:702px;height:31px;border-top:1px solid var(--line);display:flex;align-items:center}
.nav a{position:absolute;font-size:7px;color:#444;text-decoration:none}
.search{left:538px;top:68px;width:92px;height:20px;border:1px solid #ccc;border-radius:10px;font-size:7px;color:#333;padding:6px 10px}
.cart{left:635px;top:67px;width:22px;height:22px;border:1px solid #ccc;border-radius:50%;display:flex;align-items:center;justify-content:center}
.crumb{top:92px;left:0;width:702px;height:23px;background:var(--teal-band);font-size:7px;color:#fff;padding:7px 0 0 82px;font-weight:500}
.map{top:115px;left:0;width:702px;height:285px;background:linear-gradient(135deg,#ecebe6,#e2e1dc 60%,#d9e2e6)}

/* contact band */
.contact-band{top:400px;left:0;width:702px;height:352px;background:linear-gradient(120deg,#37cbb7,#2fbea9 55%,#2aa999)}
.card{left:43px;top:433px;width:337px;height:287px;background:#fff}
.card h2{position:absolute;left:30px;top:25px;font-size:17px;font-weight:700;color:#111}
.field{position:absolute;left:30px;width:278px;height:24px;border:1px solid var(--teal);background:var(--field);display:flex}
.field i{width:24px;background:var(--teal);display:flex;justify-content:center;padding-top:6px}
.field span{font-size:6.5px;color:#777;padding:8px 0 0 8px}
.field.message span{padding-top:9px}
.submit{position:absolute;left:30px;top:236px;width:278px;height:24px;background:var(--teal);color:#fff;font-size:9px;font-weight:700;display:flex;align-items:center;justify-content:center}
.hours{left:420px;top:430px;width:232px;color:#fff;text-align:center}
.hours h3{font-size:14px;font-weight:500;margin-top:50px}
.hours p{font-size:11px;line-height:15px;margin-top:8px;font-weight:300}
.hours table{margin:22px 0 0 28px;width:178px;border-collapse:collapse;font-size:8.5px;text-align:left}
.hours td{height:25px;border-bottom:1px solid rgba(255,255,255,.25)}
.hours td+td{font-weight:700;text-align:right;padding-right:10px}
.hours tr:last-child td{border-bottom:0}

/* inquiries */
.inquiry{top:776px;width:200px}
.inquiry h4{position:absolute;left:53px;top:7px;font-size:11px;font-weight:700;letter-spacing:.3px;white-space:nowrap}
.inquiry .num{position:absolute;left:53px;top:30px;font-size:11px;color:var(--teal-dark);font-weight:500}
.inquiry .mail{position:absolute;left:53px;top:49px;font-size:7.5px;color:#333}
.divider{top:785px;width:1px;height:50px;background:var(--line)}
.social{top:866px;left:293px;display:flex;gap:7px}
.social span{width:24px;height:24px;border:1.5px solid #888;border-radius:50%}

/* footer */
.footer{top:918px;left:0;width:702px;height:174px;background:var(--foot);color:#fff}
.footer .about{position:absolute;left:146px;top:10px;width:410px;font-size:8.3px;line-height:12.5px;text-align:center}
.foot-row{position:absolute;top:81px;font-size:8.3px;line-height:12.5px;display:flex;gap:8px}
.foot-links{position:absolute;top:120px;left:158px;display:flex;gap:14px;font-size:9.5px}
.foot-links .support{text-align:center}
.foot-links .support small{display:block;font-size:5.8px;line-height:8.5px}
.footer-base{top:1092px;left:0;width:702px;height:108px;background:var(--foot-dark);color:#fff}
.footer-base .rings{position:absolute;left:285px;top:12px;display:flex;gap:10px}
.footer-base .rings span{width:23px;height:23px;border:1px solid #ddd;border-radius:50%}
.footer-base hr{position:absolute;left:120px;top:48px;width:462px;border:0;border-top:1px solid #b3b3b3}
.footer-base .copy{position:absolute;left:307px;top:60px;display:flex;gap:8px;align-items:center;font-size:7.5px;line-height:11px}
.footer-base .copy b{width:14px;height:14px;background:#eee;display:block}
.chat-now{left:554px;top:1184px;width:129px;height:16px;background:var(--teal);color:#fff;font-size:8px;font-weight:700;padding:4px 0 0 6px;border-radius:3px 3px 0 0}
</style>
</head>
<body>

<header>
  <div class="abs account-tab"><span>SIGN UP</span><span>LOGIN</span></div>
  <div class="abs brand">
    <div class="brand-mark"></div>
    <div class="brand-name">TRAXIVEN</div>
  </div>
  <div class="abs contact-quick" style="left:470px">
    <div class="icon-ring"><svg width="11" height="10" viewBox="0 0 11 10"><path d="M1 1h9v6H5l-3 2V7H1z" fill="#2ec4b0"/></svg></div>LIVE CHAT
  </div>
  <div class="abs contact-quick" style="left:555px">
    <div class="icon-ring"><svg width="10" height="10" viewBox="0 0 10 10"><path d="M2 1l2 2-1 1.5a6 6 0 003 3L7.5 6l2 2-1.5 1.5C4 9 1 6 .5 1.5z" fill="#2ec4b0"/></svg></div><span class="phone-big">555-204-7710</span>
  </div>
  <nav class="abs nav">
    <a style="left:43px">SERVERS</a><a style="left:90px">WORKSTATIONS</a><a style="left:157px">COMPONENTS</a><a style="left:219px">VIRTUAL REALITY</a><a style="left:289px">DRONES</a><a style="left:333px">ABOUT US</a><a style="left:382px">BLOG</a><a style="left:416px">RESOURCES</a><a style="left:474px">CONTACT US</a>
  </nav>
  <div class="abs search">Search<svg style="position:absolute;right:8px;top:5px" width="9" height="9" viewBox="0 0 9 9"><circle cx="3.8" cy="3.8" r="2.8" stroke="#2ec4b0" stroke-width="1.3" fill="none"/><path d="M6 6l2.5 2.5" stroke="#2ec4b0" stroke-width="1.3"/></svg></div>
  <div class="abs cart"><svg width="11" height="10" viewBox="0 0 11 10"><path d="M1 3h9l-1 6H2z" fill="none" stroke="#2ec4b0" stroke-width="1.2"/><path d="M3 3l2-2M8 3L6 1" stroke="#2ec4b0"/></svg></div>
  <div class="abs crumb">HOME / CONTACT US</div>
</header>

<div class="abs map" role="img" aria-label="Street map showing the office location"></div>

<section class="abs contact-band" role="img" aria-label="Customer service representative wearing a headset, teal tinted"></section>

<form class="abs card">
  <h2>GET IN TOUCH</h2>
  <div class="field" style="top:66px"><i><svg width="9" height="10" viewBox="0 0 9 10"><circle cx="4.5" cy="3" r="2.2" fill="none" stroke="#fff"/><path d="M1 9.5a3.5 3.5 0 017 0" fill="none" stroke="#fff"/></svg></i><span>Enter Your Name</span></div>
  <div class="field" style="top:99px"><i><svg width="10" height="10" viewBox="0 0 10 10"><circle cx="5" cy="5" r="4" fill="none" stroke="#fff"/><circle cx="5" cy="5" r="1.6" fill="none" stroke="#fff"/></svg></i><span>Enter Your Email Address</span></div>
  <div class="field" style="top:132px"><i><svg width="7" height="11" viewBox="0 0 7 11"><rect x=".5" y=".5" width="6" height="10" rx="1" fill="none" stroke="#fff"/></svg></i><span>Enter Your Phone Number</span></div>
  <div class="field message" style="top:165px;height:62px"><i><svg width="10" height="8" viewBox="0 0 10 8"><rect x=".5" y=".5" width="9" height="7" fill="none" stroke="#fff"/><path d="M.5.5L5 4.5 9.5.5" fill="none" stroke="#fff"/></svg></i><span>Enter Your Message</span></div>
  <div class="submit">SUBMIT</div>
</form>

<section class="abs hours">
  <svg style="position:absolute;left:98px;top:4px" width="36" height="36" viewBox="0 0 36 36" fill="none" stroke="#fff" stroke-width="2"><rect x="2" y="6" width="24" height="22"/><path d="M2 12h24M8 2v7M20 2v7"/><circle cx="27" cy="27" r="7" fill="#30c2ad"/><path d="M27 23v4h3"/></svg>
  <h3>HOURS OF OPERATION</h3>
  <p>Our dedicated customer service representatives<br>are available 24/7 by phone.</p>
  <table>
    <tr><td>Monday</td><td>8:00am- 5:00pm</td></tr>
    <tr><td>Tuesday</td><td>8:00am- 5:00pm</td></tr>
    <tr><td>Wednesday</td><td>8:00am- 5:00pm</td></tr>
    <tr><td>Thursday</td><td>8:00am- 5:00pm</td></tr>
    <tr><td>Friday</td><td>8:00am- 5:00pm</td></tr>
    <tr><td>Sat-Sun</td><td>8:00am- 5:00pm</td></tr>
  </table>
</section>

<section>
  <div class="abs inquiry" style="left:43px">
    <svg width="36" height="40" viewBox="0 0 36 40" fill="none" stroke="#2ec4b0" stroke-width="1.6"><path d="M5 20a13 13 0 0126 0"/><rect x="2" y="19" width="6" height="10" rx="2"/><rect x="28" y="19" width="6" height="10" rx="2"/><path d="M31 29c0 6-6 8-12 8"/><circle cx="17" cy="37" r="2"/></svg>
    <h4>GENERAL INQUIRIES</h4><div class="num">(555)204-7710</div><div class="mail">info@traxivensys.com</div>
  </div>
  <div class="abs divider" style="left:245px"></div>
  <div class="abs inquiry" style="left:253px">
    <svg width="36" height="40" viewBox="0 0 36 40" fill="none" stroke="#2ec4b0" stroke-width="1.6"><path d="M6 4l6 6-3 4a18 18 0 0011 11l4-3 6 6-4 5C16 33 3 20 2 8z"/><circle cx="9" cy="31" r="5"/><path d="M20 8a8 8 0 018 8M20 2a14 14 0 0114 14"/></svg>
    <h4>SALES INQUIRIES</h4><div class="num">(555)204-7710</div><div class="mail">sales@traxivensys.com</div>
  </div>
  <div class="abs divider" style="left:455px"></div>
  <div class="abs inquiry" style="left:464px">
    <svg width="36" height="40" viewBox="0 0 36 40" fill="none" stroke="#2ec4b0" stroke-width="1.6"><rect x="1" y="6" width="34" height="24"/><path d="M18 30v6M11 37h14M11 14h14l-2 8H13z"/></svg>
    <h4>PURCHASING INQUIRIES</h4><div class="num">(555)204-7711</div><div class="mail">purchasing@traxivensys.com</div>
  </div>
  <div class="abs social"><span></span><span></span><span></span><span></span></div>
</section>

<footer>
  <div class="abs footer">
    <p class="about">Based in Westbrook California, Traxiven offers custom servers, storage, and workstations for local businesses in Los Angeles, Beverly Hills, Thousand Oaks, Ventura, Orange County, Santa Barbara, Oxnard, Irvine, Anaheim, and San Diego. Traxiven also offers such products to clients throughout the United States and Worldwide.</p>
    <div class="foot-row" style="left:148px"><svg width="7" height="10" viewBox="0 0 7 10"><path d="M3.5 10L.5 4a3 3 0 016 0z" fill="#fff"/></svg><span>4820 Meridian Ave.<br>Westbrook, CA 91400</span></div>
    <div class="foot-row" style="left:295px"><svg width="9" height="9" viewBox="0 0 10 10"><path d="M2 1l2 2-1 1.5a6 6 0 003 3L7.5 6l2 2-1.5 1.5C4 9 1 6 .5 1.5z" fill="#fff"/></svg><span>555-204-7710</span></div>
    <div class="foot-row" style="left:420px"><svg width="10" height="8" viewBox="0 0 10 8"><rect width="10" height="8" fill="#fff"/><path d="M0 0l5 4 5-4" stroke="#a4a4a4" fill="none"/></svg><span>sales@traxivensys.com</span></div>
    <div class="foot-links"><span>Computer Hardware</span><span>Drones</span><span>Virtual Reality</span><span>About Us</span><span class="support">Customer Support<small>Terms and Conditions</small><small>Warranty Information</small><small>Contact Us</small><small>Return Policy</small></span></div>
  </div>
  <div class="abs footer-base">
    <div class="rings"><span></span><span></span><span></span><span></span></div>
    <hr>
    <div class="copy"><b></b><span>Traxiven Systems, LLC.<br>Copyright © 2017</span></div>
  </div>
  <div class="abs chat-now">CHAT NOW<svg style="position:absolute;right:6px;top:5px" width="9" height="6" viewBox="0 0 9 6"><path d="M1 5l3.5-3.5L8 5" stroke="#fff" stroke-width="1.3" fill="none"/></svg></div>
</footer>

</body>
</html>
```